Velmo for Dental office

We are a dental office that are planning to add velmo to our treatment and we are in need of nice flyer to catch eyes.
attached is our logo and also a file that gives you a few items that are nice to place in the flyer- we are looking for two sizes, one postal card sized and one letter size. You can pick and choose from the document sent here in your design. Also find some royalty free images to be added to the flyer . Let me know if you need anything else.
PLEASE NOTE. The design needs to be more graphic and less in writing, the document attached is for you to choose what catches eyes and use it in flyer. You can add some details, bullet points , things that matter to customer but don't make the flyer too noisy, busy. The flyer color needs to be harmonious and match website colors

```html
<!DOCTYPE html>
<html lang="en">
<head>
<meta charset="utf-8">
<title>Birch Harbor Dental – Velmo Cosmetic Treatments</title>
<link rel="stylesheet" href="https://fonts.googleapis.com/css2?family=Montserrat:wght@400;600;700&display=swap">
<style>
  :root {
    --teal-dark: #176e72;
    --teal-light: #5cc1cb;
    --slate: #7f9bb6;
    --white: #ffffff;
    --paper: #ffffff;
    --skin-light: #f1ddd0;
    --skin-mid: #d8b29c;
    --hair: #3a2d28;
  }
  html, body {
    margin: 0;
    padding: 0;
    width: 924px;
    height: 1200px;
    overflow: hidden;
    background: var(--paper);
  }
  .flyer {
    position: relative;
    width: 924px;
    height: 1200px;
    overflow: hidden;
    background: var(--paper);
    font-family: "Montserrat", sans-serif;
  }
  .waves {
    position: absolute;
    left: 0;
    top: 0;
    width: 924px;
    height: 1200px;
  }
  .photo {
    position: absolute;
  }
  .photo-portrait {
    left: 32px;
    top: 20px;
    width: 528px;
    height: 520px;
    border-radius: 46% 46% 8% 8% / 40% 40% 6% 6%;
    background: radial-gradient(ellipse at 58% 42%, var(--skin-light) 0%, var(--skin-mid) 55%, rgba(216,178,156,0) 78%),
                radial-gradient(ellipse at 50% 12%, var(--hair) 0%, rgba(58,45,40,0) 45%);
  }
  .photo-treatment {
    left: 440px;
    top: 628px;
    width: 484px;
    height: 572px;
    border-radius: 48% 0 0 0 / 30% 0 0 0;
    background: radial-gradient(ellipse at 62% 48%, #f3e1d6 0%, #e3c3b2 42%, rgba(227,195,178,0.35) 70%, rgba(227,195,178,0) 85%),
                linear-gradient(180deg, rgba(70,55,45,0.55) 0%, rgba(70,55,45,0) 22%);
  }
  .brand {
    position: absolute;
    left: 520px;
    top: 54px;
    display: flex;
    align-items: center;
    gap: 16px;
  }
  .brand-mark {
    width: 86px;
    height: 86px;
    border-radius: 50%;
    background: var(--teal-dark);
  }
  .brand-name {
    color: var(--teal-dark);
    font-weight: 600;
    font-size: 25px;
    line-height: 1.15;
    margin: 0;
  }
  .headline {
    position: absolute;
    right: 50px;
    top: 186px;
    width: 300px;
    text-align: right;
    margin: 0;
  }
  .headline-line {
    display: block;
    font-weight: 700;
    font-size: 32px;
    line-height: 1.03;
  }
  .headline-line.light { color: var(--teal-light); }
  .headline-line.dark { color: var(--teal-dark); }
  .headline-rule {
    display: block;
    height: 2px;
    background: var(--teal-dark);
    margin: 9px -5px 12px 120px;
  }
  .intro-title {
    position: absolute;
    left: 50px;
    top: 570px;
    margin: 0;
    color: var(--white);
    font-weight: 700;
    font-size: 25px;
    line-height: 1.2;
  }
  .intro-frame {
    position: absolute;
    left: 42px;
    top: 617px;
    width: 438px;
    height: 142px;
  }
  .intro-text {
    position: absolute;
    left: 50px;
    top: 640px;
    width: 420px;
    margin: 0;
    color: var(--white);
    font-size: 14.6px;
    line-height: 1.55;
    text-align: justify;
  }
  .benefits-title {
    position: absolute;
    left: 50px;
    top: 794px;
    margin: 0;
    color: var(--white);
    font-weight: 700;
    font-size: 22px;
    line-height: 1.22;
  }
  .benefits-list {
    position: absolute;
    left: 50px;
    top: 860px;
    margin: 0;
    padding: 0;
    list-style: none;
    z-index: 2;
  }
  .benefits-list::before {
    content: "";
    position: absolute;
    left: 5px;
    top: 12px;
    bottom: 12px;
    border-left: 1px dashed var(--slate);
  }
  .benefits-list li {
    position: relative;
    padding-left: 22px;
    height: 31px;
    line-height: 22px;
    color: var(--white);
    font-size: 13.2px;
  }
  .benefits-list li::before {
    content: "";
    position: absolute;
    left: 0;
    top: 6px;
    width: 11px;
    height: 11px;
    border-radius: 50%;
    background: var(--slate);
  }
  .cta {
    position: absolute;
    left: 0;
    top: 1043px;
    width: 505px;
    height: 126px;
    background: var(--slate);
    box-sizing: border-box;
    padding: 16px 0 0 44px;
  }
  .cta-lead {
    margin: 0;
    color: var(--teal-dark);
    font-weight: 700;
    font-size: 19px;
    line-height: 1.2;
  }
  .cta-phone {
    margin: 4px 0 0;
    color: var(--white);
    font-weight: 700;
    font-size: 31px;
    line-height: 1.1;
    letter-spacing: 0.5px;
  }
  .cta-note {
    margin: 3px 0 0;
    color: var(--white);
    font-size: 12.5px;
    line-height: 1.35;
  }
  .cta-note strong { font-weight: 700; }
  .footer-band {
    position: absolute;
    left: 0;
    top: 1169px;
    width: 924px;
    height: 31px;
    background: var(--teal-dark);
  }
</style>
</head>
<body>
  <main class="flyer">
    <svg class="waves" viewBox="0 0 924 1200" aria-hidden="true">
      <path d="M0 495 C220 470 460 430 650 452 C780 466 860 500 924 534 L924 1200 L0 1200 Z" fill="var(--slate)"/>
      <path d="M0 530 C120 505 230 498 330 518 C470 548 560 572 700 572 C800 572 870 560 924 552 L924 1200 L0 1200 Z" fill="var(--teal-dark)"/>
    </svg>

    <div class="photo photo-portrait" role="img" aria-label="Portrait of a woman with smooth, radiant skin and hair in a low bun, touching her shoulder"></div>

    <header class="brand">
      <span class="brand-mark"></span>
      <p class="brand-name">Birch Harbor<br>Dental</p>
    </header>

    <h1 class="headline">
      <span class="headline-line light">Enhance<br>Your Smile</span>
      <span class="headline-rule"></span>
      <span class="headline-line dark">Refresh Your Look<br>with Velmo®</span>
      <span class="headline-rule"></span>
      <span class="headline-line light">Cosmetic<br>Treatments!</span>
    </h1>

    <h2 class="intro-title">Transform Your Smile<br>and Your Confidence!</h2>
    <svg class="intro-frame" viewBox="0 0 438 142" aria-hidden="true">
      <path d="M370 1 H426 Q437 1 437 12 V130 Q437 141 426 141 H0" fill="none" stroke="var(--white)" stroke-width="1.3"/>
    </svg>
    <p class="intro-text">At Birch Harbor Dental, we believe that a beautiful smile is about more than just healthy teeth. That’s why we’re proud to offer Velmo® Cosmetic treatments — to help you look and feel your best, both inside and out!</p>

    <div class="photo photo-treatment" role="img" aria-label="Young woman receiving a cosmetic injection near the lips from gloved hands"></div>

    <h2 class="benefits-title">Benefits of Velmo® at<br>Birch Harbor Dental</h2>
    <ul class="benefits-list">
      <li>Smooth away wrinkles around the eyes, forehead, and mouth</li>
      <li>Non-invasive with no downtime</li>
      <li>Safe and performed by skilled dental professionals</li>
      <li>Results that last 3-6 months</li>
      <li>Enhance your overall facial harmony and confidence</li>
    </ul>

    <section class="cta">
      <p class="cta-lead">Ready to Refresh Your Look?</p>
      <p class="cta-phone">Call (555)014-2290</p>
      <p class="cta-note">or visit <strong>birchharbordental.com</strong><br>to schedule your Velmo® consultation today!</p>
    </section>

    <div class="footer-band"></div>
  </main>
</body>
</html>
```